Property developer, money partner needs business card design using logo concept provided

Our company develops residential properties, does money lends for joint ventures in property deals and finds property deals for other money partners. We have provided a basic logo for you to work from. Any graphic or logo design on the card is to communicate development and finance collaboration. Color choice is not so important for us, but color choice does need to reflect professionalism.

```html
<!DOCTYPE html>
<html lang="en">
<head>
<meta charset="utf-8">
<title>Brightnest Property Solutions – Business Card</title>
<link href="https://fonts.googleapis.com/css2?family=Montserrat:wght@400;500;700&display=swap" rel="stylesheet">
<style>
  :root {
    --page-bg: #e9eef4;
    --card-bg: #ffffff;
    --blue-deep: #1c3f8f;
    --blue-mid: #1556ad;
    --blue-bright: #0b74c4;
    --ink-blue: #1e3f8a;
    --ink-dark: #1a1a1a;
    --white: #ffffff;
  }
  * { box-sizing: border-box; margin: 0; padding: 0; }
  html, body {
    width: 1200px; height: 1200px; overflow: hidden;
    background: var(--page-bg);
    font-family: "Montserrat", sans-serif;
  }
  .card {
    position: absolute; left: 165px;
    width: 870px; height: 512px;
    background: var(--card-bg);
    overflow: hidden;
    box-shadow: 0 8px 22px rgba(20, 40, 80, 0.18);
  }
  .card--front { top: 56px; }
  .card--back { top: 632px; }
  .card__shapes { position: absolute; inset: 0; width: 100%; height: 100%; }

  /* Brand block */
  .brand { position: absolute; text-align: center; color: var(--ink-blue); }
  .brand__disc { display: block; margin: 0 auto; border-radius: 50%;
    background: linear-gradient(135deg, var(--blue-bright), var(--blue-deep)); }
  .brand__name { font-weight: 700; letter-spacing: 0.18em; line-height: 1.15; }
  .brand__tag { font-weight: 700; letter-spacing: 0.08em; }
  .brand__acn { font-weight: 700; color: var(--ink-blue); letter-spacing: 0.12em; }

  .card--front .brand { left: 78px; top: 100px; width: 240px; }
  .card--front .brand__disc { width: 170px; height: 170px; margin-bottom: 34px; }
  .card--front .brand__name { font-size: 25px; }
  .card--front .brand__tag { font-size: 15px; }
  .card--front .brand__acn { font-size: 11px; margin-top: 3px; }

  .card--back .brand { left: 285px; top: 70px; width: 300px; }
  .card--back .brand__disc { width: 230px; height: 230px; margin-bottom: 40px; }
  .card--back .brand__name { font-size: 31px; }
  .card--back .brand__tag { font-size: 19px; }
  .card--back .brand__acn { font-size: 13px; margin-top: 4px; }

  /* Identity */
  .identity { position: absolute; right: 72px; top: 78px; text-align: right; color: var(--white); }
  .identity__name { font-weight: 500; font-size: 28px; line-height: 1.1; letter-spacing: 0.03em; text-transform: uppercase; }
  .identity__role { font-weight: 400; font-size: 22px; margin-top: 6px; }

  /* Contacts */
  .contact { position: absolute; left: 0; width: 870px; height: 26px; }
  .contact__text { position: absolute; right: 112px; top: 0; line-height: 26px;
    font-size: 20px; color: var(--ink-blue); white-space: nowrap; }
  .contact__tab { position: absolute; left: 775px; top: 0; width: 95px; height: 26px; }
  .contact--phone { top: 298px; }
  .contact--mail { top: 330px; }
  .contact--web { top: 363px; }
  .contact--place { top: 424px; }
</style>
</head>
<body>

<section class="card card--front" aria-label="Business card front">
  <svg class="card__shapes" viewBox="0 0 697 410" preserveAspectRatio="none" aria-hidden="true">
    <defs>
      <linearGradient id="frontBand" x1="0" y1="0" x2="1" y2="0.4">
        <stop offset="0" stop-color="#0b74c4"/>
        <stop offset="1" stop-color="#1c3f8f"/>
      </linearGradient>
    </defs>
    <polygon points="189,0 697,0 697,155 439,215" fill="url(#frontBand)"/>
  </svg>

  <div class="brand">
    <span class="brand__disc"></span>
    <p class="brand__name">BRIGHTNEST</p>
    <p class="brand__tag">Property Solutions</p>
    <p class="brand__acn">A.C.N 481 203 956</p>
  </div>

  <div class="identity">
    <p class="identity__name">Daniel<br>Whitford</p>
    <p class="identity__role">CEO, President</p>
  </div>

  <div class="contact contact--phone">
    <span class="contact__text">0412 708 356</span>
    <svg class="contact__tab" viewBox="0 0 95 26" aria-hidden="true">
      <rect x="0" y="1" width="95" height="24" fill="#1362b6"/>
      <rect x="0" y="1" width="24" height="24" fill="#1c3f8f"/>
      <path d="M8 7 l3 0 l1 4 l-2 1 q1 3 4 4 l1 -2 l4 1 l0 3 q-9 1 -11 -11z" fill="#fff"/>
    </svg>
  </div>
  <div class="contact contact--mail">
    <span class="contact__text">info@brightnest.com.au</span>
    <svg class="contact__tab" viewBox="0 0 95 26" aria-hidden="true">
      <rect x="0" y="1" width="95" height="24" fill="#1362b6"/>
      <rect x="0" y="1" width="24" height="24" fill="#1c3f8f"/>
      <rect x="6" y="8" width="12" height="9" fill="none" stroke="#fff" stroke-width="1.5"/>
      <path d="M6 8 l6 5 l6 -5" fill="none" stroke="#fff" stroke-width="1.5"/>
    </svg>
  </div>
  <div class="contact contact--web">
    <span class="contact__text">www.brightnest.com.au</span>
    <svg class="contact__tab" viewBox="0 0 95 26" aria-hidden="true">
      <rect x="0" y="1" width="95" height="24" fill="#1362b6"/>
      <rect x="0" y="1" width="24" height="24" fill="#1c3f8f"/>
      <circle cx="12" cy="13" r="6" fill="none" stroke="#fff" stroke-width="1.5"/>
      <ellipse cx="12" cy="13" rx="2.5" ry="6" fill="none" stroke="#fff" stroke-width="1.2"/>
      <line x1="6" y1="13" x2="18" y2="13" stroke="#fff" stroke-width="1.2"/>
    </svg>
  </div>
  <div class="contact contact--place">
    <span class="contact__text">27 Wattle Grove Rd Maleny Q 4552</span>
    <svg class="contact__tab" viewBox="0 0 95 26" aria-hidden="true">
      <rect x="0" y="1" width="95" height="24" fill="#1362b6"/>
      <rect x="0" y="1" width="24" height="24" fill="#1c3f8f"/>
      <path d="M12 20 q-6 -6 -6 -10 a6 6 0 0 1 12 0 q0 4 -6 10z" fill="#fff"/>
      <circle cx="12" cy="10" r="2.2" fill="#1c3f8f"/>
    </svg>
  </div>
</section>

<section class="card card--back" aria-label="Business card back">
  <svg class="card__shapes" viewBox="0 0 697 410" preserveAspectRatio="none" aria-hidden="true">
    <defs>
      <linearGradient id="backLeft" x1="0" y1="0" x2="1" y2="1">
        <stop offset="0" stop-color="#1c3f8f"/>
        <stop offset="1" stop-color="#0b74c4"/>
      </linearGradient>
      <linearGradient id="backRight" x1="0" y1="0" x2="1" y2="1">
        <stop offset="0" stop-color="#1c3f8f"/>
        <stop offset="1" stop-color="#0b74c4"/>
      </linearGradient>
    </defs>
    <polygon points="0,0 159,285 125,410 0,410" fill="url(#backLeft)"/>
    <polygon points="569,0 697,0 697,395 540,100" fill="url(#backRight)"/>
  </svg>

  <div class="brand">
    <span class="brand__disc"></span>
    <p class="brand__name">BRIGHTNEST</p>
    <p class="brand__tag">Property Solutions</p>
    <p class="brand__acn">A.C.N 481 203 956</p>
  </div>
</section>

</body>
</html>
```